Quillmont Energy Website
website
Quillmont Energy Website - Energy
Creative Brief
Energy
We are an internationally renowned company specializing in renewable energy. We have an extensive experience and ongoing projects for hydropower plants in several region in Asia, including Indonesia, supported by the brightest experts in their field.
• Need to be pretty, clean and very professional • Need to be light and easy to load • There are many paragraphs on information that we want to put, and some are very technical. The layout of this information needs to be as pleasing in the eye, as possible. Our sitemap is as follow: 1. Landing Page 2. About Us 2. Hydro 3. Indonesia 4. Personnel 5. Contact Us
http://orders.brandcrafthub.example/contests/harborline-blue-advisors
This will be a standard company profile site (from technical perspective) – we are not really looking for fancy or crazy animation ; but it does need to look very professional, and make a serious statement for the visitors. Please see sample of website that we like (Please do NOT exactly copy that. what we like is the LOOK and FEEL. not necessarily looking for a duplicate)

```html
<!DOCTYPE html>
<html lang="en">
<head>
<meta charset="utf-8">
<title>Quillmont Energy</title>
<link rel="stylesheet" href="https://fonts.googleapis.com/css2?family=Open+Sans:ital,wght@0,400;0,600;0,700;1,400;1,700&display=swap">
<style>
:root{
  --navy:#1f4f86;
  --navy-deep:#16396a;
  --footer-top:#3f74ad;
  --footer-bottom:#1e4c84;
  --tab:#e6f1c9;
  --tab-border:#9fbf5a;
  --tab-active:#1f4f86;
  --hero-top:#3f88d2;
  --hero-bottom:#a9cdec;
  --logo-blue:#2a6bb3;
  --text:#222;
  --link:#1f4f86;
  --field:#e8edf3;
  --white:#fff;
}
*{box-sizing:border-box;margin:0;padding:0}
html,body{width:1200px;height:969px;overflow:hidden}
body{font-family:"Open Sans",Arial,sans-serif;color:var(--text);background:var(--white);position:relative}

.hero{position:absolute;left:0;top:0;width:1200px;height:367px;
  background:linear-gradient(180deg,var(--hero-top) 0%,var(--hero-bottom) 100%)}

.brand{position:absolute;left:131px;top:0;width:314px;height:131px;background:var(--white);
  border-radius:0 0 10px 10px;box-shadow:0 2px 6px rgba(0,0,0,.25);
  display:flex;align-items:center;gap:16px;padding-left:26px}
.brand-mark{width:44px;height:44px;border-radius:50%;background:var(--logo-blue);flex:none}
.brand-name{font-size:34px;font-weight:400;color:var(--logo-blue);line-height:1}

.main-nav{position:absolute;left:498px;top:0;display:flex;gap:4px}
.main-nav a{display:block;height:26px;padding:0 20px;line-height:24px;font-size:15px;color:var(--navy);
  text-decoration:none;background:var(--tab);border:1px solid var(--tab-border);border-top:0;border-radius:0 0 6px 6px}
.main-nav a.active{background:var(--tab-active);color:var(--white);border-color:var(--navy-deep)}

.features{position:absolute;left:157px;top:411px;display:flex;gap:40px}
.feature{width:196px}
.feature-thumb{position:relative;height:100px;border:1px solid #bbb;box-shadow:0 2px 4px rgba(0,0,0,.3)}
.feature-thumb.renewable{background:linear-gradient(180deg,#5fa3dc,#a9cdec)}
.feature-thumb.hydro{background:linear-gradient(180deg,#8fb9dd,#4f739c)}
.feature-thumb.indonesia{background:linear-gradient(180deg,#7a7e86,#9e998f)}
.feature-thumb.savings{background:linear-gradient(180deg,#f4f4f4,#c3c8ce)}
.feature-label{position:absolute;left:0;right:0;bottom:0;height:28px;line-height:28px;text-align:center;
  font-size:17px;color:var(--white);background:rgba(40,40,40,.55);text-shadow:0 1px 2px #000}
.feature-date{margin-top:10px;font-size:10px;font-weight:700;font-style:italic}
.feature-text{font-size:10px;line-height:1.3}
.read-more{display:block;text-align:right;font-size:9px;font-weight:700;color:var(--link);text-decoration:underline;margin-top:4px}

.site-footer{position:absolute;left:0;top:668px;width:1200px;height:301px;
  background:linear-gradient(180deg,var(--footer-top),var(--footer-bottom));color:var(--white)}
.footer-col{position:absolute;top:14px}
.footer-heading{display:flex;align-items:center;gap:10px;font-size:18px;font-weight:700}
.footer-heading svg{flex:none}
.misc{left:131px;width:150px}
.misc ul{list-style:none;margin-top:12px}
.misc li{font-size:11px;padding:5px 0 5px 6px;border-bottom:1px solid rgba(255,255,255,.35)}
.testimonials{left:432px;width:260px}
.quote{margin-top:12px;font-size:11px;line-height:1.35;color:#dbe7f5}
.quote-author{display:block;font-weight:700;color:var(--white);margin-top:3px}
.contact{left:720px;width:310px}
.contact-form{margin-top:6px}
.contact-form label{display:block;font-size:10px;font-weight:700;margin-top:6px}
.field{width:210px;height:25px;background:var(--field);border-radius:3px;margin-top:3px}
.field.message{height:62px}
.submit{margin-top:12px;width:70px;height:26px;background:var(--navy-deep);border:1px solid #8fb0d6;
  border-radius:3px;color:var(--white);font-size:11px;font-weight:700;text-align:center;line-height:24px}
.copyright{position:absolute;left:131px;top:252px;font-size:11px;font-weight:700}
</style>
</head>
<body>

<header class="hero" role="img" aria-label="Wind turbines on green grass under a bright blue sky with clouds">
  <div class="brand">
    <span class="brand-mark"></span>
    <span class="brand-name">Quillmont Energy</span>
  </div>
  <nav class="main-nav">
    <a class="active" href="#">Home</a>
    <a href="#">About Us</a>
    <a href="#">Indonesia</a>
    <a href="#">Hydro</a>
    <a href="#">Personnel</a>
    <a href="#">Contact us</a>
  </nav>
</header>

<section class="features">
  <article class="feature">
    <div class="feature-thumb renewable" role="img" aria-label="Wind turbines in a green field"><span class="feature-label">Renewable Energy</span></div>
    <p class="feature-date">March 2010 - Norvik, Inc</p>
    <p class="feature-text">Web ads to get a 10% boost in 2010. For the first time advertisers will spend more on digital than print.<br>Long predicted, this Madison Avenue mile-stone has finally arrived thanks to a 9.6% boom in digital advertising in 2010.</p>
    <a class="read-more" href="#">READ MORE</a>
  </article>
  <article class="feature">
    <div class="feature-thumb hydro" role="img" aria-label="Hydropower dam with water"><span class="feature-label">Hydropower Plants</span></div>
    <p class="feature-date">March 2010 - Norvik, Inc</p>
    <p class="feature-text">Web ads to get a 10% boost in 2010. For the first time advertisers will spend more on digital than print.<br>Long predicted, this Madison Avenue mile-stone has finally arrived thanks to a 9.6% boom in digital advertising in 2010.</p>
    <a class="read-more" href="#">READ MORE</a>
  </article>
  <article class="feature">
    <div class="feature-thumb indonesia" role="img" aria-label="Industrial power plant in Indonesia"><span class="feature-label">Indonesia</span></div>
    <p class="feature-date">March 2010 - Norvik, Inc</p>
    <p class="feature-text">Web ads to get a 10% boost in 2010. For the first time advertisers will spend more on digital than print.<br>Long predicted, this Madison Avenue mile-stone has finally arrived thanks to a 9.6% boom in digital advertising in 2010.</p>
    <a class="read-more" href="#">READ MORE</a>
  </article>
  <article class="feature">
    <div class="feature-thumb savings" role="img" aria-label="Rolled technical plans on a desk"><span class="feature-label">Save Money</span></div>
    <p class="feature-date">March 2010 - Norvik, Inc</p>
    <p class="feature-text">Web ads to get a 10% boost in 2010. For the first time advertisers will spend more on digital than print.<br>Long predicted, this Madison Avenue mile-stone has finally arrived thanks to a 9.6% boom in digital advertising in 2010.</p>
    <a class="read-more" href="#">READ MORE</a>
  </article>
</section>

<footer class="site-footer">
  <div class="footer-col misc">
    <h3 class="footer-heading">
      <svg width="22" height="22" viewBox="0 0 24 24"><path d="M12 2l3 6.5 7 .8-5.2 4.8 1.4 7L12 17.6 5.8 21l1.4-7L2 9.3l7-.8z" fill="#f5c23a"/></svg>
      Misc.
    </h3>
    <ul>
      <li>Log In</li><li>Sign Up</li><li>Privacy of Policy</li><li>Get in touch</li>
      <li>Terms &amp; Conditions</li><li>FAQ's</li><li>About us</li>
    </ul>
  </div>
  <div class="footer-col testimonials">
    <h3 class="footer-heading">
      <svg width="24" height="20" viewBox="0 0 24 20"><path d="M2 2h20v12H9l-5 4v-4H2z" fill="#fff"/></svg>
      Testimonials:
    </h3>
    <p class="quote">Lorem ipsum dolor sit amet, consectetur adipiscin Fusce condimentum, lacus vel tristique tincidunt<span class="quote-author">Mara Delling</span></p>
    <p class="quote">Lorem ipsum dolor sit amet, consectetur adipiscin Fusce condimentum, lacus vel tristique tincidunt<span class="quote-author">Mara Delling</span></p>
    <p class="quote">Lorem ipsum dolor sit amet, consectetur adipiscin Fusce condimentum, lacus vel tristique tincidunt<span class="quote-author">Mara Delling</span></p>
  </div>
  <div class="footer-col contact">
    <h3 class="footer-heading">
      <svg width="22" height="22" viewBox="0 0 24 24"><circle cx="12" cy="12" r="10" fill="#fff"/><circle cx="12" cy="12" r="4" fill="#3f74ad"/></svg>
      Get in touch with us:
    </h3>
    <div class="contact-form">
      <label>NAME:</label><div class="field"></div>
      <label>EMAIL:</label><div class="field"></div>
      <label>MESSAGE:</label><div class="field message"></div>
      <div class="submit">SUBMIT</div>
    </div>
  </div>
  <p class="copyright">© 2010 Quillmont Energy, All RightsReserved</p>
</footer>

</body>
</html>
```